Storm Restoration Contractor needs a professional letterhead design

Looking for a professional letterhead design. Not looking for your cheapo MS Word standard ones that are readily available. Dont want it to be cookie cutter look like ones readily available online. We just recently changed our logo and want to freshen up all our documents. Our company handles restoring a property back to a pre-loss condition after a storm damages it. For example, wind, hail, flood, fire losses.

Target Market(s)

Property Owners, Homeowners, Property Owners, Commercial Property Owners, Property Management Companies

Industry/Entity Type

Construction Company

Requirements
Must have
• Professional, Use 1 of 2 logo options
• Storm Restoration, Roofing, Siding, Windows

```html
<!DOCTYPE html>
<html lang="en">
<head>
<meta charset="utf-8">
<title>Harbor Ridge Exteriors – Letterhead</title>
<link href="https://fonts.googleapis.com/css2?family=Questrial&display=swap" rel="stylesheet">
<style>
:root{
  --bg:#d9d9d9;
  --paper:#f2f2f2;
  --ink:#3a3a3a;
  --blue:#2567b3;
  --charcoal:#4e4e50;
  --rule:#c9c9c9;
  --ghost:#e6e6e6;
}
*{margin:0;padding:0;box-sizing:border-box}
html,body{width:1200px;height:1041px;overflow:hidden;background:var(--bg)}
body{font-family:"Questrial",sans-serif;color:var(--ink)}
.letterhead{position:absolute;left:200px;top:4px;width:800px;height:1033px;background:var(--paper);overflow:hidden}
.ghost-ring{position:absolute;left:548px;top:0;width:310px;height:310px;border-radius:50%;border:20px solid var(--ghost)}
.brand{position:absolute;display:flex;align-items:center;gap:10px;color:var(--blue);letter-spacing:.5px}
.brand-dot{border-radius:50%;background:var(--blue);flex:none}
.brand--header{left:59px;top:62px;font-size:22px}
.brand--header .brand-dot{width:50px;height:50px}
.brand--footer{left:59px;top:958px;font-size:12px;gap:6px}
.brand--footer .brand-dot{width:14px;height:14px}
.date{position:absolute;left:59px;top:251px;font-size:11.5px}
.recipient{position:absolute;left:59px;top:279px;font-size:11.5px;line-height:14px}
.salutation{position:absolute;left:59px;top:397px;font-size:11.5px;font-weight:bold}
.body-copy{position:absolute;left:59px;top:425px;width:682px;font-size:11.3px;line-height:14px;text-align:justify}
.body-copy p{margin-bottom:14px}
.closing{position:absolute;left:59px;top:719px;font-size:11.5px;line-height:14px}
.closing strong{display:block}
.signature{position:absolute;left:150px;top:703px;width:175px;height:85px;background:linear-gradient(135deg,#e9edf6,#dde4f2);border-radius:4px}
.footer{position:absolute;left:0;top:955px;width:800px;height:40px;font-size:11px;line-height:15px}
.footer .divider{position:absolute;top:5px;width:1px;height:24px;background:var(--rule)}
.footer .address{position:absolute;left:228px;top:3px}
.contact{position:absolute;top:3px}
.contact-row{display:flex;align-items:center;gap:6px}
.contact-row svg{width:11px;height:11px;flex:none}
.bar-dark{position:absolute;left:0;top:1014px;width:420px;height:19px;background:var(--charcoal)}
.bar-blue{position:absolute;left:412px;top:1014px;width:388px;height:19px;background:var(--blue);clip-path:polygon(0 0,8px 0,16px 10px,100% 10px,100% 100%,16px 100%,0 100%)}
</style>
</head>
<body>
<main class="letterhead">
  <div class="ghost-ring"></div>

  <div class="brand brand--header"><span class="brand-dot"></span><span>Harbor Ridge Exteriors</span></div>

  <p class="date">30.09.2016</p>
  <p class="recipient">Recipient’s name<br>Lindenweg 12<br>10115 Musterstadt<br>Germany</p>

  <p class="salutation">Dear sir,</p>

  <div class="body-copy">
    <p>Communication is a very integral part of living creatures, animals and humans. Communication may be verbal or written. Written communication however is only applicable to human beings. Can you even imagine a world without communication? Verbal communication can be through telephones, webcams or in person. Written communication is through letters, emails and mobile phone messages.</p>
    <p>In today’s world of great inventions and technology, letters have somehow become redundant. It is the time for text messages or chats. But they still can communicate a lot more than all other modes of communication. Organizations and various government departments still bank on letters as a strong medium of communication. There is no comparison in costs of sending letters as compared to costs of mobile phone messages though – letters are far cheaper. Letters now commonly known as “hard copy documents” are considered more relevant and important than email copies of text messages as proof or evidence of some sort.</p>
    <p>Letters speak volumes about a person or an organization that writes it. So one must take utmost care ensuring that the language used in any letter is appropriate for the occasion for which it is being written. Since a letter is also a written proof or document, if there are certain things that should not form a part of it, then that too should be carefully handled.</p>
    <p>Writing a good letter is an art. But if for some reason someone is unable to write that perfect letter, these different types of letters provide a base for you to build on. Sample letters have been given for everyone to understand what all information needs to form a part of the letter type and then it can be customized.</p>
  </div>

  <p class="closing">Yours Sincerely,<strong>Dana Whitlow</strong></p>
  <div class="signature" role="img" aria-label="Handwritten signature in blue ink"></div>

  <footer class="footer">
    <span class="divider" style="left:193px"></span>
    <p class="address">4410 E Canyon Mesa Drive STE 210<br>Mesa Vista, AZ 85090</p>
    <span class="divider" style="left:413px"></span>
    <div class="contact" style="left:450px">
      <div class="contact-row"><svg viewBox="0 0 12 12"><rect width="12" height="12" rx="2" fill="#2567b3"/><path d="M3.5 2.5l1.5 1.5-.8 1c.5 1 1.3 1.8 2.3 2.3l1-.8 1.5 1.5-1 1C5.5 9 3 6.5 2.5 4.5z" fill="#fff"/></svg>555-010-4400</div>
      <div class="contact-row"><svg viewBox="0 0 12 12"><rect width="12" height="12" rx="2" fill="#2567b3"/><rect x="3" y="2.5" width="6" height="3" fill="#fff"/><rect x="2.5" y="6" width="7" height="3.5" fill="#fff"/></svg>555-010-4490</div>
    </div>
    <span class="divider" style="left:572px"></span>
    <div class="contact" style="left:608px">
      <div class="contact-row"><svg viewBox="0 0 12 12"><rect width="12" height="12" rx="2" fill="#2567b3"/><rect x="2.5" y="3.5" width="7" height="5" fill="none" stroke="#fff"/><path d="M2.5 3.5L6 6.5 9.5 3.5" fill="none" stroke="#fff"/></svg>hello@harborridgeext.com</div>
      <div class="contact-row"><svg viewBox="0 0 12 12"><rect width="12" height="12" rx="2" fill="#2567b3"/><circle cx="6" cy="6" r="3.5" fill="none" stroke="#fff"/><path d="M2.5 6h7M6 2.5v7" stroke="#fff"/></svg>www.harborridgeext.com</div>
    </div>
  </footer>
  <div class="brand brand--footer"><span class="brand-dot"></span><span>Harbor Ridge Exteriors</span></div>

  <div class="bar-dark"></div>
  <div class="bar-blue"></div>
</main>
</body>
</html>
```